Information security software developer needs new product website

We are Quorvane - and we have created an anti-ransomware application that we think is pretty special.
Our product is now updating to version 2, bringing in a slew of new features that we want to showcase through this website.

The site itself should communicate trust and safety, be blue  (#22b8eb) and white and be themed around security, protection, shields and calmness. Due to the complex nature of the product, we will be creating a number of gifs to show usage of the features - the design needs to account for these gifs alongside feature headings.

Ideally, some graphics that communicate the themes of security and protection can be used throughout the design rather then technology photos - ultimately we don't want to scare people into using our product, we want it to feel like a trusted platform that makes sense to use.

you can read about us here - docs.quorvane-example.io to get an idea of what we do!

```html
<!DOCTYPE html>
<html lang="en">
<head>
<meta charset="utf-8">
<title>Quorvane Access Manager</title>
<link rel="stylesheet" href="https://fonts.googleapis.com/css2?family=Roboto:wght@400;500;700&family=Lato:wght@400;700&display=swap">
<style>
  :root {
    --brand: #22b8eb;
    --brand-deep: #1a9fd0;
    --ink: #2b2b2b;
    --muted: #555a60;
    --slate: #7b8b97;
    --footer: #1c1d22;
    --white: #ffffff;
  }
  * { box-sizing: border-box; margin: 0; padding: 0; }
  html, body { width: 1200px; height: 3196px; overflow: hidden; background: var(--white); }
  body { position: relative; font-family: "Roboto", sans-serif; color: var(--ink); }
  .abs { position: absolute; }

  /* header */
  .site-header { position: relative; z-index: 3; }
  .brand { left: 112px; top: 30px; display: flex; align-items: center; gap: 12px; }
  .brand-mark { width: 34px; height: 34px; background: var(--brand-deep); border-radius: 4px; }
  .brand-name { font-family: "Roboto", sans-serif; font-size: 50px; font-weight: 500; color: var(--brand-deep); line-height: 1; }
  .nav { left: 481px; top: 50px; font-size: 13px; font-weight: 700; }
  .nav a { text-decoration: none; color: var(--ink); position: absolute; white-space: nowrap; }
  .nav a.active { color: var(--brand); }

  .hero-art { left: 546px; top: 48px; width: 654px; height: 665px; z-index: 1;
    background: radial-gradient(circle at 55% 55%, #f4c860 0 12%, #9a7a4c 13% 28%, #57b8ee 29% 60%, #22b8eb 61%);
    border-radius: 62% 0 0 48% / 40% 0 0 60%; }

  .hero-title { left: 109px; top: 214px; width: 440px; font-size: 44px; font-weight: 700; line-height: 47px; color: var(--ink); }
  .hero-text { left: 112px; top: 426px; width: 430px; font-size: 13.5px; line-height: 22px; color: var(--muted); }
  .btn { display: flex; align-items: center; justify-content: center; border-radius: 24px; font-size: 13.5px; font-weight: 700; text-transform: uppercase; }
  .btn-primary { left: 112px; top: 509px; width: 144px; height: 47px; background: var(--brand); color: var(--white); }
  .product-tag { left: 292px; top: 512px; display: flex; align-items: center; gap: 12px; }
  .product-tag .mark { width: 40px; height: 44px; background: var(--brand-deep); border-radius: 6px; }
  .product-tag .label { font-size: 18px; line-height: 20px; color: var(--ink); }
  .product-tag .label small { display: block; font-size: 12px; color: var(--brand-deep); font-weight: 500; }

  /* features */
  .features-title { left: 0; width: 1200px; top: 804px; text-align: center; font-size: 40px; font-weight: 700; color: var(--ink); }
  .feature { width: 300px; text-align: center; }
  .feature .ring { width: 186px; height: 186px; margin: 0 auto; border: 4px solid var(--brand); border-radius: 50%;
    display: flex; align-items: center; justify-content: center; }
  .feature h3 { margin-top: 16px; font-size: 21px; font-weight: 500; line-height: 30px; color: var(--ink); white-space: nowrap; }
  .feature svg { width: 110px; height: 110px; fill: none; stroke: #111; stroke-width: 3; stroke-linejoin: round; stroke-linecap: round; }

  /* about */
  .about-band { left: 0; top: 1545px; width: 1200px; height: 577px; background: var(--brand); }
  .about-photo { left: 0; top: 1545px; width: 550px; height: 577px; border-radius: 0 30px 30px 0;
    background: linear-gradient(135deg, #3d5670 0%, #2b3a4c 45%, #9aa3ab 70%, #d8d3cb 100%); }
  .about-title { left: 599px; top: 1620px; font-size: 40px; font-weight: 700; color: var(--white); }
  .about-copy { left: 599px; top: 1686px; width: 495px; font-size: 13.5px; line-height: 22.3px; color: var(--white); }
  .about-copy p + p { margin-top: 22px; }
  .btn-light { left: 599px; top: 1973px; width: 144px; height: 47px; background: var(--white); color: var(--brand); }

  /* defend */
  .defend-title { left: 111px; top: 2218px; font-size: 39px; font-weight: 700; line-height: 47px; color: var(--ink); white-space: nowrap; }
  .defend-copy { left: 112px; top: 2386px; width: 490px; font-size: 13.5px; line-height: 22.3px; color: var(--muted); }
  .btn-slate { left: 112px; top: 2664px; width: 145px; height: 48px; background: var(--slate); color: var(--white); }
  .defend-photo { left: 634px; top: 2225px; width: 454px; height: 487px; border-radius: 40px;
    background: linear-gradient(120deg, #e6ecef 0%, #b9c6cc 40%, #5b6670 70%, #2f3338 100%); }

  .chat { left: 1105px; top: 2785px; width: 56px; height: 56px; border-radius: 50%; background: var(--brand); display: flex; align-items: center; justify-content: center; z-index: 2; }

  /* footer */
  .footer { left: 0; top: 2814px; width: 1200px; height: 382px; background: var(--footer); font-family: "Lato", sans-serif; color: var(--white); }
  .footer .brand { left: 112px; top: 106px; }
  .footer .brand-mark { background: var(--white); width: 36px; height: 36px; }
  .footer .brand-name { color: var(--white); font-size: 46px; font-weight: 400; }
  .socials { left: 110px; top: 174px; display: flex; gap: 4px; }
  .socials span { width: 36px; height: 36px; border-radius: 50%; background: var(--white); }
  .foot-col h4 { font-family: "Lato", sans-serif; font-size: 18px; font-weight: 700; margin-bottom: 14px; }
  .foot-col ul { list-style: none; font-size: 13px; line-height: 22.3px; }
  .foot-col li::before { content: "»"; margin-right: 9px; }
  .col-company { left: 395px; top: 89px; }
  .col-help { left: 609px; top: 89px; }
  .col-news { left: 815px; top: 89px; width: 280px; }
  .col-news p { font-size: 13px; line-height: 22.3px; }
  .news-input { left: 815px; top: 195px; width: 273px; height: 44px; background: var(--white); display: flex; align-items: center; justify-content: space-between; padding: 0 16px; font-size: 13px; color: #888; }
  .foot-rule { left: 112px; top: 292px; width: 976px; height: 1px; background: #4a4b50; }
  .copyright { left: 0; width: 1200px; top: 318px; text-align: center; font-size: 13px; }
</style>
</head>
<body>

<header class="site-header">
  <div class="abs brand"><span class="brand-mark"></span><span class="brand-name">Quorvane</span></div>
  <nav class="abs nav">
    <a class="active" style="left:0">HOME</a>
    <a style="left:66px">ABOUT US</a>
    <a style="left:159px">SERVICES</a>
    <a style="left:249px">BLOG</a>
    <a style="left:311px">CONTACT US</a>
  </nav>
</header>

<section class="hero">
  <div class="abs hero-art" role="img" aria-label="Illustration of a cloud with a laptop full of labelled folders, a padlock, a globe and small figures working on security"></div>
  <h1 class="abs hero-title">We have created an anti-ransomware application that we think is pretty special</h1>
  <p class="abs hero-text">Quorvane Access Manager is a tool that allows you to safely delegate sensitive administrative access to computers in your Corvex Directory environment in a modern and user-friendly way.</p>
  <a class="abs btn btn-primary">Get Started</a>
  <div class="abs product-tag"><span class="mark"></span><span class="label"><small>Quorvane</small>Access Manager</span></div>
</section>

<section class="features">
  <h2 class="abs features-title">OUR FEATURES</h2>

  <div class="abs feature" style="left:124px;top:886px">
    <div class="ring"><svg viewBox="0 0 110 110"><path d="M40 50V38a15 15 0 0 1 30 0v12"/><rect x="34" y="50" width="42" height="14" rx="2"/><rect x="10" y="66" width="90" height="28" rx="4"/><path d="M24 72v16M17 76l14 8M17 84l14-8M44 72v16M37 76l14 8M37 84l14-8M64 72v16M57 76l14 8M57 84l14-8M84 72v16M77 76l14 8M77 84l14-8"/></svg></div>
    <h3>Web-based access to local<br>admin passwords</h3>
  </div>
  <div class="abs feature" style="left:450px;top:886px">
    <div class="ring"><svg viewBox="0 0 110 110"><rect x="10" y="16" width="90" height="78" rx="6"/><path d="M10 32h90"/><circle cx="20" cy="24" r="3"/><circle cx="30" cy="24" r="3"/><path d="M48 28l6-10h38"/><path d="M47 56v-6a8 8 0 0 1 16 0v6"/><rect x="43" y="56" width="24" height="14"/><rect x="28" y="74" width="54" height="14"/><path d="M40 78l4 6M36 81h12M55 78v6M50 81h10M68 78l4 6M64 81h12"/></svg></div>
    <h3>Access historical local<br>admin passwords</h3>
  </div>
  <div class="abs feature" style="left:782px;top:886px">
    <div class="ring"><svg viewBox="0 0 110 110"><rect x="14" y="10" width="82" height="58" rx="4"/><rect x="22" y="18" width="66" height="42"/><path d="M34 36l8-8M38 40l12-12"/><path d="M50 68v10h10V68M36 80h38"/><path d="M18 86h74l4 12H14z"/><path d="M26 92h58"/></svg></div>
    <h3>Just-in-time administrative<br>access to computers</h3>
  </div>

  <div class="abs feature" style="left:124px;top:1178px">
    <div class="ring"><svg viewBox="0 0 110 110"><rect x="8" y="16" width="94" height="70" rx="3"/><path d="M8 30h94"/><circle cx="18" cy="23" r="2"/><circle cx="26" cy="23" r="2"/><circle cx="34" cy="23" r="2"/><path d="M22 46v16M15 50l14 8M15 58l14-8M44 46v16M37 50l14 8M37 58l14-8"/><path d="M68 62v-8a10 10 0 0 1 20 0v8"/><rect x="62" y="62" width="32" height="30" rx="3"/><circle cx="78" cy="74" r="4"/><path d="M78 78v6"/></svg></div>
    <h3>Easy access to DriveSeal<br>recovery passwords</h3>
  </div>
  <div class="abs feature" style="left:450px;top:1178px">
    <div class="ring"><svg viewBox="0 0 110 110"><rect x="18" y="18" width="64" height="82" rx="6"/><path d="M38 18v-6h24v6h6v8H32v-8z"/><circle cx="50" cy="14" r="3"/><rect x="28" y="38" width="12" height="12"/><path d="M31 44l3 3 5-6"/><rect x="28" y="58" width="12" height="12"/><path d="M31 64l3 3 5-6"/><rect x="28" y="78" width="12" height="12"/><path d="M31 84l3 3 5-6"/><path d="M46 44h14M46 64h10M46 84h16"/><path d="M96 24l-28 34-6 12 12-6 28-34z"/></svg></div>
    <h3>Audit success and failure<br>event logs</h3>
  </div>
  <div class="abs feature" style="left:776px;top:1178px">
    <div class="ring"><svg viewBox="0 0 110 110"><path d="M22 10h44l14 14v74H22z"/><path d="M66 10v14h14"/><circle cx="40" cy="32" r="10"/><path d="M43 27h-5a2.5 2.5 0 0 0 0 5h4a2.5 2.5 0 0 1 0 5h-6M40 24v16"/><path d="M30 52h24M30 60h20M30 68h18M30 76h18"/><circle cx="66" cy="68" r="12"/><path d="M60 64h12M60 68h12M60 72h12"/><path d="M75 77l14 14"/></svg></div>
    <h3>Modern authentication<br>options</h3>
  </div>
</section>

<section class="about">
  <div class="abs about-band"></div>
  <div class="abs about-photo" role="img" aria-label="Photo of hands typing on a laptop showing a sign-in screen, with a glass of coffee beside it"></div>
  <h2 class="abs about-title">ABOUT US</h2>
  <div class="abs about-copy">
    <p>Quorvane Access Manager is a tool that allows you to safely delegate sensitive administrative access to computers in your Corvex Directory environment in a modern and user-friendly way.</p>
    <p>It provides a web-based interface that allows users to request local admin passwords, driveseal recovery keys, and grant just-in-time administrative access to their own accounts.</p>
    <p>It is fully compatible and works out-of-the-box with Veltrosoft KeyRotate, or you can replace the Veltrosoft KeyRotate agent with the Quorvane Access Manager Agent, which encrypts local admin passwords in the directory, and can optionally save a history of local admin passwords.</p>
  </div>
  <a class="abs btn btn-light">Learn More</a>
</section>

<section class="defend">
  <h2 class="abs defend-title">Defend against ransomware<br>and other lateral movement<br>-based attacks</h2>
  <p class="abs defend-copy">Access Manager has one simple goal. To reduce the likelihood and impact of a wide-spread compromise in your environment by removing permanent administrative access to your workstations and servers. By making sure every computer has a unique local admin password (through the use of Veltrosoft KeyRotate or the Quorvane Access Manager Agent), and removing all other members of the built-in local Administrators group, you can limit the ability for credential-stealing ransomware to move laterally across your environment. Access Manager makes it as seamless as possible for admins to access KeyRotate passwords, or grant themselves temporary just-in-time admin access. Access Manager isn't a silver bullet guaranteed to protect you from these sort of attacks, but it forms a fundamental part of a defence-in-depth strategy against them.</p>
  <a class="abs btn btn-slate">Learn More</a>
  <div class="abs defend-photo" role="img" aria-label="Photo of a person in an office pointing at a computer screen"></div>
</section>

<div class="abs chat"><svg width="28" height="26" viewBox="0 0 28 26"><path d="M14 2C7 2 2 6.5 2 12c0 3 1.5 5.5 4 7.3L5 24l6-3c1 .2 2 .3 3 .3 7 0 12-4.5 12-10S21 2 14 2z" fill="#fff"/></svg></div>

<footer class="abs footer">
  <div class="abs brand"><span class="brand-mark"></span><span class="brand-name">Quorvane</span></div>
  <div class="abs socials"><span></span><span></span><span></span><span></span></div>
  <div class="abs foot-col col-company">
    <h4>Company</h4>
    <ul><li>About us</li><li>Careers</li><li>News</li><li>Inventory</li></ul>
  </div>
  <div class="abs foot-col col-help">
    <h4>Help</h4>
    <ul><li>Terms &amp; condition</li><li>FAQ</li><li>Privacy policy</li><li>Search</li></ul>
  </div>
  <div class="abs foot-col col-news">
    <h4>Newsletter</h4>
    <p>Lorem ipsum dolor sit amet, consectetur adipi scing elit, sed do eiusmod tempor</p>
  </div>
  <div class="abs news-input"><span>Email address</span><svg width="16" height="16" viewBox="0 0 16 16"><path d="M1 7l14-6-5 14-2-6z" fill="#22b8eb"/></svg></div>
  <div class="abs foot-rule"></div>
  <p class="abs copyright">© Copyrights Company name 2021. All rights reserved | Privacy policy | Terms Condition</p>
</footer>

</body>
</html>
```